Brochure Design for Healthy Restaurant in Canada

We are looking for a brochure designed , that is clean , and can incorporate a couple of our food photos, as well as a QR code. We want to ensure every single item and category that we have is on the brochure and not missed . Ensure spelling is correct, as well as the pricing. We are a healthy lifestyle kitchen, that serves dine in, take out, delivery and meal prep services. We are not looking for weights or anything like that in the brochure, but we would like some greenery. If you go to the website , you will see the descriptions that we would like to have under each and every item. Please ensure you click CALGARY location. Thanks

Industry/Entity Type

Restaurant , and hospitality

Requirements
Must have
• Logo, photos and QR code for website. Also a ad that says "download our app! " with the vendly hub and pixel bazaar icons. Also , please put our address "Unit 305-4819 61st Street NE, Calgary AB, T3P 7W9

```html
<!DOCTYPE html>
<html lang="en">
<head>
<meta charset="utf-8">
<title>Sprigwell Healthy Kitchen – Menu Brochure</title>
<link rel="stylesheet" href="https://fonts.googleapis.com/css2?family=Oswald:wght@400;500&family=Montserrat:wght@500;600;700;800&family=Open+Sans:ital,wght@0,400;1,400&family=Roboto:wght@400;700&display=swap">
<style>
:root{
  --green:#8cc63f;
  --ink:#231f20;
  --muted:#5a5a5a;
  --ghost:#ececec;
  --paper:#ffffff;
  --backdrop:#e4e4e4;
  --placeholder:#e6e6e6;
}
*{margin:0;padding:0;box-sizing:border-box}
html,body{width:1200px;height:1200px;overflow:hidden}
body{background:var(--backdrop);position:relative;font-family:"Open Sans",sans-serif;color:var(--ink)}
.sheet{position:absolute;width:696px;height:537px;background:var(--paper);overflow:hidden}
.sheet--outside{left:69px;top:56px}
.sheet--inside{left:440px;top:620px}
.abs{position:absolute}
.photo{position:absolute}
.ghost{position:absolute;font-family:"Montserrat",sans-serif;font-weight:500;color:var(--ghost);font-size:28px;letter-spacing:1px;line-height:1;white-space:nowrap}
.cat{font-family:"Montserrat",sans-serif;font-weight:600;color:var(--green);font-size:9.4px;letter-spacing:.3px;line-height:1.08;margin-bottom:3px;position:relative}
.item{margin-bottom:4.2px}
.item-head{display:flex;justify-content:space-between;align-items:flex-start;gap:4px}
.item-name{font-family:"Oswald",sans-serif;font-weight:500;font-size:6.3px;line-height:7.6px;letter-spacing:.1px;text-transform:uppercase}
.price{font-family:"Oswald",sans-serif;font-weight:400;font-size:6.3px;line-height:7.6px;white-space:nowrap}
.desc{font-style:italic;font-size:5.1px;line-height:6.4px;color:var(--muted)}
.rule-v{position:absolute;border-left:1px dashed #b8b8b8}
.rule-h{position:absolute;border-top:1px dashed #b8b8b8}
.app-band{position:absolute;left:232px;top:0;width:464px;height:252px;background:var(--green)}
.app-badge-circle{position:absolute;left:353px;top:88px;width:80px;height:80px;border-radius:50%;background:var(--paper);display:flex;align-items:center;justify-content:center;text-align:center;font-family:"Oswald",sans-serif;font-weight:500;color:var(--green);font-size:12.5px;line-height:14px}
.store{position:absolute;left:265px;width:63px;height:17px;background:#111;border-radius:3px;color:#fff;display:flex;align-items:center;gap:4px;padding-left:5px;font-family:"Roboto",sans-serif;font-size:7px;font-weight:700}
.store i{display:block;width:7px;height:7px;border-radius:50%;background:#fff}
.brand{position:absolute;text-align:center}
.brand-name{font-family:"Montserrat",sans-serif;font-weight:800;color:#6d6e71;letter-spacing:1px;line-height:1}
.brand-line{font-family:"Montserrat",sans-serif;font-weight:700;color:var(--green);line-height:1;margin-top:3px;white-space:nowrap}
.address{position:absolute;left:264px;top:484px;font-family:"Roboto",sans-serif;font-size:9.2px;line-height:12.4px;color:#444}
.hours{position:absolute;right:79px;top:484px;text-align:right;font-family:"Roboto",sans-serif;font-weight:700;font-size:9.2px;line-height:12.4px;color:var(--green)}
.qr-box{position:absolute;left:627px;top:467px;width:50px;height:50px;background:var(--placeholder)}
.kids{position:absolute;left:138px;top:196px;width:76px;height:322px;background:var(--paper);border:1px dashed var(--green);text-align:center;z-index:2}
.kids-head{background:var(--green);color:#fff;font-family:"Montserrat",sans-serif;font-weight:600;font-size:9.4px;height:26px;display:flex;align-items:center;justify-content:center}
.kids-list{padding:4px 6px 0}
.kids .item{margin-bottom:5px}
.kids .item-name,.kids .price{display:block}
.build{position:absolute;left:369px;top:164px;width:94px;height:117px;background:var(--green);color:#fff;text-align:center;padding-top:9px}
.build-title{font-family:"Montserrat",sans-serif;font-weight:500;font-size:8.8px;line-height:10px;margin-bottom:5px}
.build-opt{border-top:1px dashed rgba(255,255,255,.85);padding:5px 0 6px;font-family:"Oswald",sans-serif;font-size:5.8px;line-height:7.6px}
</style>
</head>
<body>

<section class="sheet sheet--outside">
  <div class="photo" style="left:0;top:0;width:232px;height:94px;background:linear-gradient(100deg,#6b4a2c,#c9883f 45%,#7a9a3c 75%,#d9a440)" role="img" aria-label="Photo of two stacked burgers with lettuce, tomato and cheese"></div>
  <div class="abs" style="left:17px;top:33px;width:112px;height:80px;background:var(--paper)"></div>

  <div class="ghost" style="left:3px;top:180px">PIZZA</div>
  <div class="ghost" style="left:3px;top:384px;line-height:.95">TREAT &amp;<br>SNACKS</div>

  <div class="abs" style="left:25px;top:43px;width:93px">
    <h2 class="cat">BURGERS</h2>
    <div class="item"><div class="item-head"><span class="item-name">Double Stack Burger</span><span class="price">$00.00</span></div><p class="desc">Two 3oz juicy beef patties, sliced real chedder, ketchup, 1/2 fat mayo, SHK pickled onions, lettuce,tomato, served with traditional bun.</p></div>
    <div class="item"><div class="item-head"><span class="item-name">Cajun Chicken Burger</span><span class="price">$00.00</span></div><p class="desc">Marinated cajun spiced chicken, sliced swiss cheese, tomato, lettuce, spicy mayo, served on a traditional burger bun.</p></div>
    <div class="item"><div class="item-head"><span class="item-name">SHK Bison Burger</span><span class="price">$00.00</span></div><p class="desc">Bison patty, lettuce, tomato, cheddar cheese, chipotle mayo, and an egg on a whole wheat burger bun.</p></div>
  </div>

  <div class="abs" style="left:25px;top:190px;width:93px">
    <h2 class="cat">PIZZA</h2>
    <div class="item"><div class="item-head"><span class="item-name">BBQ Steak Pizza</span><span class="price">$00.00</span></div><p class="desc">Evenly brushed with a BBQ base, topped with Shaved rib eye steak, mozzarella cheese, cherry tomato, mushrooms, drizzled with our SHK ranch.</p></div>
    <div class="item"><div class="item-head"><span class="item-name">Pesto Pizza</span><span class="price">$00.00</span></div><p class="desc">An even spread of pesto for the base, topped with diced chicken, cherry tomato, and mozzarella cheese.</p></div>
    <div class="item"><div class="item-head"><span class="item-name">Margarita Pizza</span><span class="price">$00.00</span></div><p class="desc">Fresh tomato sauce base, bocconcini, fresh basil.</p></div>
    <div class="item"><div class="item-head"><span class="item-name">Classic Chicken Pizza</span><span class="price">$00.00</span></div><p class="desc">An even spread of fresh tomato sauce, diced chicken, mushrooms, pepper mix, caramelized onion, and mozzarella cheese.</p></div>
    <div class="item"><div class="item-head"><span class="item-name">Garden Veggie Pizza</span><span class="price">$00.00</span></div><p class="desc">Fresh tomato sauce base, mozzarella cheese, caramelized onion, mushrooms, pepper mix, garnished with arugula.</p></div>
  </div>

  <div class="abs" style="left:25px;top:400px;width:93px">
    <h2 class="cat">TREATS &amp; SNACKS</h2>
    <div class="item"><div class="item-head"><span class="item-name">Coconut Cream Cookie</span><span class="price">$00.00</span></div><p class="desc">Coconut cream filled sandwich cookie.</p></div>
    <div class="item"><div class="item-head"><span class="item-name">Cranberry Pecan Oats</span><span class="price">$00.00</span></div><p class="desc">Organic rolled oats infused overnight.</p></div>
    <div class="item"><div class="item-head"><span class="item-name">Peanut Butter Oats</span><span class="price">$00.00</span></div><p class="desc">Organic rolled oats infused overnight.</p></div>
    <div class="item"><div class="item-head"><span class="item-name">Protein Carrot Cake</span><span class="price">$00.00</span></div><p class="desc">Fresh house made dessert cake.</p></div>
    <div class="item"><div class="item-head"><span class="item-name">White Chocolate Brownie Bites</span><span class="price">$00.00</span></div><p class="desc">Irresistible hand rolled treats.</p></div>
  </div>

  <div class="rule-v" style="left:129px;top:118px;height:404px"></div>

  <div class="abs" style="left:137px;top:117px;width:78px">
    <h2 class="cat">FRESH JUICES</h2>
    <div class="item"><div class="item-head"><span class="item-name">Strawberry Mint</span><span class="price">$00.00</span></div><p class="desc">Strawberries, mint leaves, lemon, celery, &amp; apple</p></div>
    <div class="item"><div class="item-head"><span class="item-name">Citrus Carrot</span><span class="price">$00.00</span></div><p class="desc">Mint leaves, carrots, lemon, orange, &amp; apple.</p></div>
    <div class="item"><div class="item-head"><span class="item-name">Daily Green</span><span class="price">$00.00</span></div><p class="desc">Kale, cucumber, ginger, lemon, &amp; apple.</p></div>
    <div class="item"><div class="item-head"><span class="item-name">Golden Turmeric</span><span class="price">$00.00</span></div><p class="desc">Turmeric, carrot, lemon, orange, &amp; apple.</p></div>
    <div class="item"><div class="item-head"><span class="item-name">Beet Root</span><span class="price">$00.00</span></div><p class="desc">Beet, carrot, lemon, ginger, kale, &amp; apple.</p></div>
  </div>

  <div class="abs" style="left:137px;top:282px;width:78px">
    <h2 class="cat">PROTEIN<br>SMOOTHIES</h2>
    <div class="item"><div class="item-head"><span class="item-name">Walnut Crunch</span><span class="price">$00.00</span></div><p class="desc">Walnuts, almond butter, cinnamon, dates, greek yogurt, unsweetened almond milk, and vanilla whey protein.</p></div>
    <div class="item"><div class="item-head"><span class="item-name">Mango Rise</span><span class="price">$00.00</span></div><p class="desc">Mango, pineapple, banana, apple juice, coconut water, vanilla whey protein.</p></div>
    <div class="item"><div class="item-head"><span class="item-name">Green Glow</span><span class="price">$00.00</span></div><p class="desc">Spinach, dates, cinnamon, almond butter, banana, coconut water, and vanilla whey protein.</p></div>
    <div class="item"><div class="item-head"><span class="item-name">Maple Peanut Butter</span><span class="price">$00.00</span></div><p class="desc">Peanut butter, banana, vanilla extract, maple syrup, unsweetened almond milk, and vanilla whey protein.</p></div>
    <div class="item"><div class="item-head"><span class="item-name">Berry Bright</span><span class="price">$00.00</span></div><p class="desc">Blueberries, strawberries, raspberries, pineapple, coconut water, and vanilla whey protein.</p></div>
    <div class="item"><div class="item-head"><span class="item-name">Strawberry Tango</span><span class="price">$00.00</span></div><p class="desc">Strawberry, banana, mango, vanilla extract, honey, almond milk, and vanilla whey protein.</p></div>
  </div>

  <div class="app-band"></div>
  <div class="photo" style="left:265px;top:104px;width:166px;height:234px;border-radius:8px;background:linear-gradient(160deg,#3d3d3d,#7a6a58 45%,#c9c9c9)" role="img" aria-label="Three smartphones showing the ordering app and meal prep screens"></div>
  <div class="app-badge-circle">DOWNLOAD<br>OUR APP!</div>
  <div class="store" style="top:316px"><i></i>vendly hub</div>
  <div class="store" style="top:340px"><i></i>pixel bazaar</div>

  <div class="photo" style="left:481px;top:32px;width:196px;height:340px;background:linear-gradient(170deg,#5c4a3e,#3a3330 40%,#8a7a5c 70%,#4f5a3a)" role="img" aria-label="Photo of a poached egg bowl with avocado and mushrooms above packed meal prep containers"></div>

  <div class="brand" style="left:259px;top:412px;width:160px">
    <div class="brand-name" style="font-size:24px">SPRIGWELL</div>
    <div class="brand-line" style="font-size:8.6px">HEALTHY KITCHEN&nbsp;|&nbsp;MEAL PREP</div>
  </div>
  <div class="brand" style="left:481px;top:391px;width:197px">
    <div class="brand-name" style="font-size:30px">SPRIGWELL</div>
    <div class="brand-line" style="font-size:10.6px">HEALTHY KITCHEN&nbsp;|&nbsp;MEAL PREP</div>
  </div>

  <div class="rule-h" style="left:248px;top:470px;width:369px"></div>
  <svg class="abs" style="left:250px;top:484px" width="8" height="11" viewBox="0 0 8 11" aria-hidden="true"><path d="M4 0.5C2 0.5 .6 2 .6 3.9 .6 6.5 4 10.5 4 10.5S7.4 6.5 7.4 3.9C7.4 2 6 .5 4 .5Z" fill="none" stroke="#8cc63f" stroke-width="1.2"/><circle cx="4" cy="3.9" r="1.2" fill="#8cc63f"/></svg>
  <p class="address">Unit 305-4819 61st Street NE<br>Calgary AB, T3P 7W9</p>
  <p class="hours">Monday – Saturday<br>9AM–8PM</p>
  <div class="qr-box" role="img" aria-label="QR code linking to the website"></div>
</section>

<section class="sheet sheet--inside">
  <div class="ghost" style="left:2px;top:16px">SALADS</div>
  <div class="ghost" style="left:234px;top:16px">PENNE</div>
  <div class="ghost" style="left:558px;top:16px">BRUNCH</div>

  <div class="abs" style="left:25px;top:27px;width:188px">
    <h2 class="cat">SALADS</h2>
    <div class="item"><div class="item-head"><span class="item-name">Cajun Chicken Pecan Salad</span><span class="price">$00.00</span></div><p class="desc">Fresh chicken breast, spring mixed lettuce, tomato, cranberries, pecans, diced bell peppers, feta cheese, served with a hoisin vinaigrette.</p></div>
    <div class="item"><div class="item-head"><span class="item-name">Salmon Avocado Salad</span><span class="price">$00.00</span></div><p class="desc">Fresh Salmon, baby spinach, avocado, strawberries, red onions, goat cheese, &amp; sliced almonds, served with a balsamic vinaigrette.</p></div>
    <div class="item"><div class="item-head"><span class="item-name">Sesame Ahi Tuna Salad</span><span class="price">$00.00</span></div><p class="desc">Pistachio crusted Ahi Tuna loin, celery, red onion, bell peppers, roasted cashews, spring mix lettuce, served with a house made sesame ginger vinaigrette.</p></div>
    <div class="item"><div class="item-head"><span class="item-name">Chicken Caesar Salad</span><span class="price">$00.00</span></div><p class="desc">Freshly baked chicken breast, bacon, chopped romaine lettuce, house made croutons, shaved parmesan, served with our SHK caesar dressing.</p></div>
    <div class="item"><div class="item-head"><span class="item-name">Mediterranean Chicken</span><span class="price">$00.00</span></div><p class="desc">Fresh baked chicken, grilled pineapple, red onion, cucumber, arugula, cherry tomatoes, red radish, house made orange citrus dressing, served with our SHK mediterranean topping.</p></div>
  </div>

  <div class="rule-h" style="left:25px;top:196px;width:97px"></div>
  <div class="abs" style="left:25px;top:206px;width:97px">
    <h2 class="cat">PLANT BASED</h2>
    <div class="item"><div class="item-head"><span class="item-name">Tofu Veggie Plate</span><span class="price">$00.00</span></div><p class="desc">Broccoli, cauliflower, peppers, celery, carrot, onion, chickpeas, tofu, over a bed of brown rice or quinoa, with a choice of thai or teriyaki sauce.</p></div>
    <div class="item"><div class="item-head"><span class="item-name">Chili Guac Plate</span><span class="price">$00.00</span></div><p class="desc">Vegan Chilli Mix, Guacamole, Salsa, Baby Corn Salad, served with Tortilla Chips.</p></div>
    <div class="item"><div class="item-head"><span class="item-name">Garden Patty Burger</span><span class="price">$00.00</span></div><p class="desc">House made veggie patty, lettuce, Tomato, Vegan Mayo, Ketchup.</p></div>
    <div class="item"><div class="item-head"><span class="item-name">Cauli Mash Plate</span><span class="price">$00.00</span></div><p class="desc">Cauliflower Mash, Arugula Salad, House Made Paradise mix.</p></div>
    <div class="item"><div class="item-head"><span class="item-name">Eggplant Harvest</span><span class="price">$00.00</span></div><p class="desc">SHK plant based bites, roasted seasoned eggplant steaks, edamame hummus, cherry tomatoes, served with our house made orange carrot sauce.</p></div>
  </div>

  <div class="photo" style="left:0;top:394px;width:232px;height:143px;background:linear-gradient(120deg,#c94a3a,#e8d8c0 40%,#f3ece0 60%,#b86a3a)" role="img" aria-label="Photo of a yogurt parfait with granola, cherries and berries"></div>

  <aside class="kids">
    <div class="kids-head">KIDS</div>
    <div class="kids-list">
      <div class="item"><span class="item-name">Small Burger<br>w/ Fruit</span><span class="price">$00.00</span><p class="desc">Lettuce, tomato, ketchup and mustard, served on a whole wheat burger bun.</p></div>
      <div class="item"><span class="item-name">Mini Pasta w/<br>Chicken</span><span class="price">$00.00</span><p class="desc">Baked chicken with penne pasta, and a choice of pesto or tomato sauce &amp; a parmesan cheese garnish.</p></div>
      <div class="item"><span class="item-name">Mini Mac &amp; Cheese</span><span class="price">$00.00</span><p class="desc">SHK cheese sauce with broccoli and tomato, served over penne pasta.</p></div>
      <div class="item"><span class="item-name">Mini Cocoa<br>Pancakes</span><span class="price">$00.00</span><p class="desc">Dark chocolate chips, house made chocolate sauce with banana and 100% maple syrup.</p></div>
      <div class="item"><span class="item-name">Mini Berry Waffles</span><span class="price">$00.00</span><p class="desc">Fresh strawberries and blueberries, strawberry yogurt sauce, served with 100% maple syrup.</p></div>
    </div>
  </aside>

  <div class="abs" style="left:250px;top:27px;width:99px">
    <h2 class="cat">PENNE PASTA</h2>
    <div class="item"><div class="item-head"><span class="item-name">Tomato Basil Pasta</span><span class="price">$00.00</span></div><p class="desc">Organic farro penne pasta or fettuccini, tomato sauce, parmesan, peppers, broccoli &amp; a parmesan cheese garnish.</p></div>
    <div class="item"><div class="item-head"><span class="item-name">Bolognese Pasta</span><span class="price">$00.00</span></div><p class="desc">Organic farro penne pasta or fettuccini, house made meat sauce, parmesan, peppers, broccoli &amp; a parmesan cheese garnish.</p></div>
    <div class="item"><div class="item-head"><span class="item-name">Pesto &amp; Parmesan Pasta</span><span class="price">$00.00</span></div><p class="desc">Organic farro penne pasta or fettuccini, pesto sauce, parmesan, peppers, broccoli &amp; a parmesan cheese garnish.</p></div>
    <div class="item"><div class="item-head"><span class="item-name">Penne &amp; Cheese</span><span class="price">$00.00</span></div><p class="desc">Organic farro penne pasta or fettuccini, SHK cheese sauce, broccoli, tomato.</p></div>
  </div>

  <div class="rule-h" style="left:250px;top:196px;width:99px"></div>
  <div class="abs" style="left:250px;top:206px;width:99px">
    <h2 class="cat">BOWLS &amp; MAINS</h2>
    <div class="item"><div class="item-head"><span class="item-name">Peanut Pineapple Bowl</span><span class="price">$00.00</span></div><p class="desc">Freshly baked chicken breast, no dairy mashed potato, grilled pineapple, wilted bok choy, topped off with our creamy house made peanut pineapple sauce.</p></div>
    <div class="item"><div class="item-head"><span class="item-name">Chicken Demi Plate</span><span class="price">$00.00</span></div><p class="desc">Oven baked chicken, asparagus, mushrooms, dairy free mashed potato, served with our signature SHK demi glace.</p></div>
    <div class="item"><div class="item-head"><span class="item-name">Sweet Potato Taco Bowl</span><span class="price">$00.00</span></div><p class="desc">Ground beef, oven roasted sweet potato, spinach, avocado, monterey jack cheese, drizzled with ancho chipotle, and sour cream.</p></div>
    <div class="item"><div class="item-head"><span class="item-name">Creamy Ahi Tuna Plate</span><span class="price">$00.00</span></div><p class="desc">Ahi tuna loin, carrots, broccoli, housemade creamy florentine sauce.</p></div>
    <div class="item"><div class="item-head"><span class="item-name">Coconut Garlic Shrimp</span><span class="price">$00.00</span></div><p class="desc">Shrimp, bok choy, cauliflower, broccoli, green beans, house made coconut garlic sauce.</p></div>
    <div class="item"><div class="item-head"><span class="item-name">Teriyaki Steak Bowl</span><span class="price">$00.00</span></div><p class="desc">Asparagus, broccoli, green beans, steak bites, coconut brown rice, and gluten free teriyaki sauce.</p></div>
    <div class="item"><div class="item-head"><span class="item-name">Sesame Ginger Bowl</span><span class="price">$00.00</span></div><p class="desc">Roasted chicken breast, Ginger Shrimp, red onion, avocado, carrot, green beans, brown rice, cashews, house made hummus, house made sesame ginger dressing.</p></div>
    <div class="item"><div class="item-head"><span class="item-name">Shrimp Stir Fry</span><span class="price">$00.00</span></div><p class="desc">Shrimp, bok choy, peppers, broccoli, celery, onion, brown rice or quinoa, teriyaki or thai sauce choice.</p></div>
  </div>

  <div class="photo" style="left:369px;top:0;width:186px;height:164px;background:radial-gradient(ellipse at 55% 55%,#a8552a,#6b4a34 45%,#d8d2c6 75%,#4a4a42)" role="img" aria-label="Photo of a seared chicken breast with mushrooms, mash and asparagus"></div>

  <div class="build">
    <div class="build-title">BUILD YOUR<br>MEAL</div>
    <div class="build-opt">CHICKEN BREAST<br>$00.00</div>
    <div class="build-opt">SALMON<br>$00.00</div>
    <div class="build-opt">STRIPLOIN STEAK<br>$00.00</div>
  </div>

  <div class="abs" style="left:369px;top:292px;width:83px">
    <h2 class="cat">PROTEIN<br>PANCAKES &amp;<br>WAFFLES</h2>
    <div class="item"><div class="item-head"><span class="item-name">Dark Cocoa Pancakes</span><span class="price">$00.00</span></div><p class="desc">Gluten free protein pancake mix, dark chocolate chips, banana, house made chocolate sauce, served with 100% maple syrup.</p></div>
    <div class="item"><div class="item-head"><span class="item-name">Blueberry Stack Pancakes</span><span class="price">$00.00</span></div><p class="desc">Gluten free protein pancake mix, fresh blueberries, blueberry yogurt sauce, served with 100% maple syrup.</p></div>
    <div class="item"><div class="item-head"><span class="item-name">Mixed Berry Waffle</span><span class="price">$00.00</span></div><p class="desc">Gluten free protein waffle mix, fresh blueberries and strawberries, strawberry yogurt sauce, and 100% maple syrup.</p></div>
    <div class="item"><div class="item-head"><span class="item-name">Banana Cocoa Waffle</span><span class="price">$00.00</span></div><p class="desc">Gluten free pancake mix, topped with roasted banana, SHK granola, house made chocolate sauce, served with 100% maple syrup.</p></div>
  </div>

  <div class="abs" style="left:568px;top:27px;width:102px">
    <h2 class="cat">BRUNCH</h2>
    <div class="item"><div class="item-head"><span class="item-name">Sunny Egg Bowl</span><span class="price">$00.00</span></div><p class="desc">Our famous turkey bites, arugula, cherry tomato, avocado, mushrooms, caramelized onions, roasted potato, poached egg, topped with signature SHK, no butter hollandaise sauce.</p></div>
    <div class="item"><div class="item-head"><span class="item-name">Bacon Egg Sandwich</span><span class="price">$00.00</span></div><p class="desc">Toasted multigrain bun, with applewood bacon, caramelized onions, mushrooms, egg, finished with our SHK ranch sauce.</p></div>
    <div class="item"><div class="item-head"><span class="item-name">Scramble Toast</span><span class="price">$00.00</span></div><p class="desc">Perfectly toasted multi-seed bread, with scrambled egg, caramelized onion, finely diced pepper mix, SHK candied goat cheese, house made guacamole, topped off with our signature hollandaise sauce.</p></div>
  </div>

  <div class="abs" style="left:482px;top:173px;width:188px">
    <div class="item"><div class="item-head"><span class="item-name">Margarita Omelette</span><span class="price">$00.00</span></div><p class="desc">Cherry tomatoes, bocconcini, fresh Basil, with perfectly toasted multigrain bread.</p></div>
    <div class="item"><div class="item-head"><span class="item-name">Steak &amp; Bacon Omelette</span><span class="price">$00.00</span></div><p class="desc">Shaved rib eye steak, applewood bacon, caramelized onion, mozzarella cheese, served with toasted multigrain bread.</p></div>
    <div class="item"><div class="item-head"><span class="item-name">Steak Bean Burrito</span><span class="price">$00.00</span></div><p class="desc">Shaved rib eye steak, black beans, caramelized onions, cherry tomatoes, feta cheese, SHK ranch, all wrapped in a whole wheat tortilla.</p></div>
    <div class="item"><div class="item-head"><span class="item-name">Smoked Salmon Toast</span><span class="price">$00.00</span></div><p class="desc">Perfectly toasted multi-seed bread, layered with cream cheese, red onion, capers, and smoked sockeye salmon.</p></div>
    <div class="item"><div class="item-head"><span class="item-name">Blueberry Parfait</span><span class="price">$00.00</span></div><p class="desc">SHK granola, blueberries, grapefruit, greek vanilla yogurt, mint, drizzled with maple syrup, topped with cherries.</p></div>
    <div class="item"><div class="item-head"><span class="item-name">Chocolate Banana Parfait</span><span class="price">$00.00</span></div><p class="desc">SHK granola, vanilla greek yogurt, roasted banana, house made chocolate sauce, garnished with crumbled amaretti cookie, and strawberries.</p></div>
    <div class="item"><div class="item-head"><span class="item-name">Steak &amp; Eggs Set</span><span class="price">$00.00</span></div><p class="desc">6oz Striploin Steak, Salsa Scrambled Eggs, &amp; Whole Wheat Toast.</p></div>
  </div>

  <div class="rule-h" style="left:482px;top:356px;width:188px"></div>
  <div class="abs" style="left:482px;top:365px;width:188px">
    <h2 class="cat">BETWEEN BREADS</h2>
    <div class="item"><div class="item-head"><span class="item-name">Pineapple BBQ Wrap</span><span class="price">$00.00</span></div><p class="desc">Chicken breast, bell peppers, tomato, cheese, pineapple, red onion, spinach, bbq sauce.</p></div>
    <div class="item"><div class="item-head"><span class="item-name">Chipotle Steak Wrap</span><span class="price">$00.00</span></div><p class="desc">Ancho Chipotle sauce, bell peppers, red onion, tomato, spinach, cheese, and steak bites.</p></div>
    <div class="item"><div class="item-head"><span class="item-name">Chicken Pesto Panini</span><span class="price">$00.00</span></div><p class="desc">Chicken breast, pesto spread, avocado, tomatoes, mozzarella cheese.</p></div>
    <div class="item"><div class="item-head"><span class="item-name">Thai Shrimp Wrap</span><span class="price">$00.00</span></div><p class="desc">Marinated shrimp, spinach, monterey jack cheese, cashews, house made thai sauce.</p></div>
    <div class="item"><div class="item-head"><span class="item-name">Chicken Pesto Quesadilla</span><span class="price">$00.00</span></div><p class="desc">Chicken breast, pesto spread, tomato, onions, bell peppers, cheese, whole wheat tortilla.</p></div>
    <div class="item"><div class="item-head"><span class="item-name">Chicken Tzatziki Wrap</span><span class="price">$00.00</span></div><p class="desc">Baked chicken breast, house made tzatziki dressing, bacon, tomato, lettuce, farro, whole wheat tortilla.</p></div>
  </div>
</section>

</body>
</html>
```